Local water manufacturing needs a re-design to an existing label design.

We need to change an existing label design for an established water manufacturing company located in the Bahamas. We are expanding into a new 1.5L size product and would like to do so with an updated label design that incorporates an animated pink conch shell (sample included) with at least one other bright color to match the existing blue background and the pink conch shell. The final design should convey an island feel and vibe. The existing label is only a suggestion. The entire label can be completely changed.

Target Market(s)

Hotels, tourist

Industry/Entity Type

Water Manufacturing

Requirements
Must have
• Bright color that matches blue cap and pink conch shell
Nice to have
• Simple design with sleek modern look.

```html
<!DOCTYPE html>
<html lang="en">
<head>
<meta charset="utf-8">
<title>Coralis Purified Water Label</title>
<link rel="stylesheet" href="https://fonts.googleapis.com/css2?family=Poppins:wght@300;400;600;700;800&family=Roboto+Condensed:wght@400;700&display=swap">
<style>
  :root {
    --magenta: #c8128a;
    --cream: #f7e6d8;
    --navy: #0e2f5a;
    --sky-top: #5cdbfb;
    --sky-low: #ffffff;
    --sea: #0fc6dd;
    --sea-deep: #0aa7c4;
    --sand: #f8e6c0;
    --sand-light: #fdf1da;
    --shell-pink: #f7b6dd;
  }
  * { margin: 0; padding: 0; box-sizing: border-box; }
  html, body { width: 720px; height: 1200px; overflow: hidden; }
  body { font-family: "Poppins", sans-serif; color: var(--navy); }

  .label {
    position: relative;
    width: 720px;
    height: 1200px;
    overflow: hidden;
  }
  .beach-scene {
    position: absolute;
    inset: 0;
    background: linear-gradient(to bottom,
      var(--sky-top) 0%,
      #bdf0fd 25%,
      var(--sky-low) 46%,
      var(--sky-low) 49%,
      var(--sea-deep) 50%,
      var(--sea) 56%,
      #aeeef2 60%,
      var(--sand) 64%,
      var(--sand-light) 80%,
      var(--sand) 100%);
  }

  /* rotated frame: u runs bottom-to-top, v runs left-to-right */
  .frame {
    position: absolute;
    left: 0;
    top: 1200px;
    width: 1200px;
    height: 720px;
    transform-origin: 0 0;
    transform: rotate(-90deg);
  }

  .brand-band {
    position: absolute;
    left: 388px;
    top: 54px;
    width: 812px;
    height: 236px;
    background: var(--magenta);
  }
  .brand-name {
    position: absolute;
    left: 528px;
    top: 54px;
    width: 536px;
    height: 236px;
    display: flex;
    align-items: center;
    justify-content: center;
    font-family: "Poppins", sans-serif;
    font-weight: 700;
    font-size: 112px;
    letter-spacing: 1px;
    color: var(--cream);
  }

  .conch-art {
    position: absolute;
    left: 312px;
    top: 72px;
    width: 184px;
    height: 208px;
    border-radius: 48% 52% 40% 60% / 55% 45% 55% 45%;
    background: radial-gradient(ellipse at 55% 60%, var(--shell-pink) 0%, #fbe0ee 55%, #fff3f8 100%);
  }

  .product-title {
    position: absolute;
    left: 700px;
    top: 300px;
    width: 352px;
    text-align: right;
    color: var(--navy);
  }
  .product-title .type {
    font-weight: 600;
    font-size: 38px;
    line-height: 46px;
    white-space: nowrap;
  }
  .product-title .sub {
    font-weight: 300;
    font-size: 23px;
    line-height: 30px;
    letter-spacing: 0.5px;
    white-space: nowrap;
  }

  .info-block {
    position: absolute;
    left: 704px;
    color: var(--navy);
    white-space: nowrap;
  }
  .info-block h3 {
    font-weight: 700;
    font-size: 16px;
    line-height: 22px;
  }
  .info-block p {
    font-weight: 400;
    font-size: 14.5px;
    line-height: 23px;
  }
  .bottler { top: 480px; }
  .contact { top: 566px; }
  .contact p { font-size: 16px; line-height: 25px; }

  .nutrition {
    position: absolute;
    left: 312px;
    top: 474px;
    width: 346px;
    color: var(--navy);
    font-family: "Roboto Condensed", sans-serif;
    font-size: 9.5px;
    line-height: 12px;
  }
  .nutrition h2 {
    font-family: "Poppins", sans-serif;
    font-weight: 800;
    font-size: 25px;
    line-height: 28px;
    white-space: nowrap;
  }
  .nutrition .cols {
    display: flex;
    gap: 10px;
  }
  .nutrition .col { flex: 1; }
  .nutrition .row {
    display: flex;
    justify-content: space-between;
    white-space: nowrap;
  }
  .nutrition .rule { border-top: 2px solid var(--navy); margin: 3px 0; }
  .nutrition .rule.thin { border-top-width: 1px; }
  .nutrition .right { text-align: right; }
  .nutrition .note { font-size: 7.5px; white-space: nowrap; margin-top: 2px; }
</style>
</head>
<body>
<div class="label">
  <div class="beach-scene" role="img" aria-label="Illustrated tropical beach: bright sky, turquoise sea and sandy shore with starfish and seashells"></div>

  <div class="frame">
    <div class="brand-band"></div>
    <div class="brand-name">Coralis</div>
    <div class="conch-art" role="img" aria-label="Illustrated pink conch shell"></div>

    <div class="product-title">
      <div class="type">PURIFIED WATER</div>
      <div class="sub">MINERALS ADDED</div>
    </div>

    <div class="info-block bottler">
      <h3>Bottled by:</h3>
      <p>Reefline Ltd, t/a Coralis Water &amp; Tidal Water.</p>
      <p>PO BOX KQ-10482</p>
    </div>

    <div class="info-block contact">
      <h3>Call For More Info:</h3>
      <p>sales:555-0142</p>
      <p>office:55-0198</p>
    </div>

    <div class="nutrition">
      <h2>Nutrition Facts</h2>
      <div class="cols">
        <div class="col">
          <div class="row"><span>Serving Size &nbsp;ml</span></div>
          <div class="row"><span>Serving Per Container</span></div>
          <div class="rule"></div>
          <div class="row"><span>Amount Per Serving</span></div>
          <div class="row"><span>Calories &nbsp;Cal</span></div>
          <div class="rule thin"></div>
          <div class="right">% Daily Value*</div>
          <div class="rule thin"></div>
          <div class="row"><span>Total Fat &nbsp;g . . . . . . . .</span><span>%*</span></div>
          <div class="row"><span>Saturated Fat &nbsp;g . . . . . .</span><span>%*</span></div>
        </div>
        <div class="col">
          <div class="row"><span>Sodium &nbsp;mg . . . . . . . . . .</span><span>%*</span></div>
          <div class="rule"></div>
          <div class="row"><span>Total Carb &nbsp;g . . . . . . .</span><span>%*</span></div>
          <div class="row"><span>Dietary Fiber &nbsp;g . . . . . .</span><span>%*</span></div>
          <div class="row"><span>Sugars &nbsp;g</span></div>
          <div class="rule"></div>
          <div class="row"><span>Protein &nbsp;g</span></div>
          <div class="rule"></div>
          <div class="note">*Percent Daily Values are based on a (&nbsp;&nbsp;&nbsp;) calorie diet.</div>
        </div>
      </div>
    </div>
  </div>
</div>
</body>
</html>
```